Bright Tooth Dentistry Business Card

We need business cards for our dental office.
We are looking for a clean, elegant design

We provide dental services to children.
Our card needs to be appealing to referring dentists, parents and our team

Target Market(s)

referring dentists, parents and our team

Industry/Entity Type

Dental Clinic

Contact Information for Business Card

4816 Juniper Lane, Suite 100
Cedar Hollow, PA 15237

412-837-2961 Voice
412-837-2962 fax
info@brighttoothdentalpa.com email
www.brighttoothdentalpa.com web

Font styles to use
Sans Serif

Requirements
Must have
• White background - clean, crisp, elegant, simple
• rounded corners
• different color palate - once we come up with design, we will replace the blue with orange, green,
Nice to have
• Follow our logo typeface and colors
• then we can replace color

```html
<!DOCTYPE html>
<html lang="en">
<head>
<meta charset="utf-8">
<title>Bright Tooth Dentistry – Business Card</title>
<link rel="stylesheet" href="https://fonts.googleapis.com/css2?family=Source+Sans+3:wght@400;600&display=swap">
<style>
  :root {
    --brand-blue: #00aeef;
    --ink: #1b1b1f;
    --paper: #ffffff;
    --canvas: #ffffff;
    --shadow: rgba(0, 0, 0, 0.35);
  }
  * { box-sizing: border-box; margin: 0; padding: 0; }
  html, body {
    width: 1200px; height: 960px; overflow: hidden;
    background: var(--canvas);
    font-family: "Source Sans 3", sans-serif;
    color: var(--ink);
  }
  .card {
    position: absolute;
    left: 286px;
    width: 629px;
    height: 359px;
    border-radius: 24px;
    box-shadow: 0 2px 6px var(--shadow);
    overflow: hidden;
  }
  .card--front { top: 109px; background: var(--paper); }
  .card--back  { top: 492px; background: var(--brand-blue); }

  .brand-name {
    font-family: "Source Sans 3", sans-serif;
    font-weight: 600;
    white-space: nowrap;
    line-height: 1;
  }
  .card--front .brand-name {
    position: absolute;
    right: 23px;
    top: 111px;
    font-size: 34px;
    color: var(--brand-blue);
  }
  .card--back .brand-name {
    position: absolute;
    left: 0; right: 0;
    top: 200px;
    text-align: center;
    font-size: 38px;
    color: var(--paper);
  }

  .address {
    position: absolute;
    left: 44px;
    top: 183px;
    font-size: 17px;
    line-height: 27px;
    font-style: normal;
  }

  .rules { position: absolute; left: 0; top: 0; }

  .contact {
    position: absolute;
    font-size: 17px;
    line-height: 27px;
    list-style: none;
  }
  .contact--phone { left: 43px; top: 266px; }
  .contact--web   { left: 336px; top: 264px; }
  .contact .label { display: inline-block; width: 20px; }
  .contact .sep   { margin-right: 4px; }
</style>
</head>
<body>

<section class="card card--front" aria-label="Card front">
  <div class="brand-name">Bright Tooth Dentistry</div>

  <address class="address">
    4816 Juniper Lane, Suite 100<br>
    Cedar Hollow, PA 15237
  </address>

  <svg class="rules" width="629" height="359" viewBox="0 0 629 359" aria-hidden="true">
    <g fill="var(--brand-blue)">
      <rect x="21" y="247" width="585" height="2"/>
      <rect x="21" y="247" width="44" height="4"/>
      <rect x="562" y="247" width="44" height="4"/>
      <rect x="21" y="335" width="585" height="2"/>
      <rect x="21" y="333" width="44" height="4"/>
      <rect x="562" y="333" width="44" height="4"/>
      <rect x="313" y="256" width="2" height="73"/>
    </g>
  </svg>

  <ul class="contact contact--phone">
    <li><span class="label">P</span><span class="sep">:</span>412-837-2961</li>
    <li><span class="label">F</span><span class="sep">:</span>412-837-2962</li>
  </ul>
  <ul class="contact contact--web">
    <li><span class="label">E</span><span class="sep">:</span>info@brighttoothdentalpa.com</li>
    <li><span class="label">W</span><span class="sep">:</span>www.brighttoothdentalpa.com</li>
  </ul>
</section>

<section class="card card--back" aria-label="Card back">
  <div class="brand-name">Bright Tooth Dentistry</div>
</section>

</body>
</html>
```